Electrical contractor in San Diego county since 1988

Provide a company name/ logo for business cards and forms. Newer and more modern old card is attached. Color preference is black and orange. Simple and streamlined nothing too busy. I have also attached a card that represents the simplicity of what we are looking for.

Contractor

```html
<!DOCTYPE html>
<html lang="en">
<head>
<meta charset="utf-8">
<title>K.T. Power INC. – Business Card</title>
<link href="https://fonts.googleapis.com/css2?family=Montserrat:wght@400;500;600&display=swap" rel="stylesheet">
<style>
  :root {
    --orange: #ee7a2f;
    --ink: #1d1d1d;
    --band: #262626;
    --paper: #ffffff;
    --muted: #b9b9b9;
    --backdrop: #e9e6e0;
  }
  * { box-sizing: border-box; margin: 0; padding: 0; }
  html, body {
    width: 1200px; height: 800px; overflow: hidden;
    background: var(--backdrop);
    font-family: "Montserrat", sans-serif;
  }
  .card {
    position: absolute; left: 150px; top: 143px;
    width: 900px; height: 514px;
    background: var(--paper);
    display: flex; flex-direction: column;
    box-shadow: 0 10px 30px rgba(0,0,0,0.18);
  }
  .card__accent { height: 16px; background: var(--orange); }
  .card__identity {
    flex: 1;
    display: flex; flex-direction: column; align-items: center;
    padding-top: 46px;
    color: var(--ink);
  }
  .mark {
    display: flex; align-items: center; gap: 12px;
    color: var(--orange); font-weight: 600; font-size: 22px;
    letter-spacing: 0.5px;
  }
  .mark__circle {
    width: 30px; height: 30px; border-radius: 50%;
    border: 3px solid var(--orange);
  }
  .license { margin-top: 36px; font-size: 11px; font-weight: 500; letter-spacing: 0.3px; }
  .company { margin-top: 6px; font-size: 27px; font-weight: 500; letter-spacing: 0.5px; }
  .tagline { margin-top: 10px; font-size: 13px; font-weight: 500; letter-spacing: 0.4px; }
  .card__contacts {
    height: 196px; background: var(--band);
    display: flex; align-items: center; justify-content: space-between;
    padding: 0 70px;
    color: var(--muted); font-size: 14px; font-weight: 500; letter-spacing: 0.6px;
  }
  .contact { display: flex; align-items: flex-start; gap: 14px; line-height: 1.35; }
  .contact__icon { width: 16px; height: 16px; margin-top: 2px; fill: var(--orange); flex: none; }
  .contact__name { text-transform: uppercase; }
</style>
</head>
<body>
  <article class="card">
    <div class="card__accent"></div>
    <section class="card__identity">
      <div class="mark"><span class="mark__circle"></span>K.T. Power</div>
      <p class="license">Lic. 000000</p>
      <h1 class="company">K.T. Power INC.</h1>
      <p class="tagline">Commercial - New &amp; Remodel</p>
    </section>
    <section class="card__contacts">
      <div class="contact">
        <svg class="contact__icon" viewBox="0 0 16 16" aria-hidden="true"><circle cx="8" cy="4.5" r="3.5"/><path d="M1 16c0-4 3-6.5 7-6.5s7 2.5 7 6.5z"/></svg>
        <div><div class="contact__name">Dana Mercer</div><div>President</div></div>
      </div>
      <div class="contact">
        <svg class="contact__icon" viewBox="0 0 16 16" aria-hidden="true"><path d="M8 0a5.5 5.5 0 0 0-5.5 5.5C2.5 10 8 16 8 16s5.5-6 5.5-10.5A5.5 5.5 0 0 0 8 0zm0 7.8a2.3 2.3 0 1 1 0-4.6 2.3 2.3 0 0 1 0 4.6z"/></svg>
        <div><div>P.O. Box 4720</div><div>Fairview, CA 90000 - 0000</div></div>
      </div>
      <div class="contact">
        <svg class="contact__icon" viewBox="0 0 16 16" aria-hidden="true"><path d="M3.6 0.8l2.4 2.9-1.5 2a9.5 9.5 0 0 0 5.8 5.8l2-1.5 2.9 2.4-1.7 2.6C8 15.5 0.5 8 1 2.5z"/></svg>
        <div><div>(555) 014 - 2087</div><div>FAX: 014 - 2088</div></div>
      </div>
    </section>
  </article>
</body>
</html>
```